Bluefinch Painting needs a Website

We need a website built for a Painting company I own, we mainly do residential painting, but don't want to be limited to that.

Need to have estimate request form.
Need pic's of past projects

I like the look of the website for http://www.harborline-painters.example
& "Wexley Property inspections"

My logo that was designed here on ArtHive on the front page

I would like one of the houses I downloaded as part of the background
of the front page.

Target Market(s)

Home owners

Industry/Entity Type

Painting

Number of Pages Required

1 page

Font styles to use
Serif

Requirements
Must have
• Estimate request form for home owners to fill out -
• Name:
• Phone Number:
• Address:
• E-mail:
• Painting project description:
• And my info to:
• My phone number: (555) 318-7046
• My web address bluefinchpainting.example
Nice to have
• My logo that was designed here on ArtHive

```html
<!DOCTYPE html>
<html lang="en">
<head>
<meta charset="utf-8">
<title>Bluefinch Painting</title>
<link href="https://fonts.googleapis.com/css2?family=Lora:wght@400;700&family=Noto+Serif:wght@400;700&display=swap" rel="stylesheet">
<style>
:root{
  --cyan:#3ec3f0;
  --blue:#1b72bd;
  --navy:#124a7e;
  --ink:#333333;
  --muted:#666666;
  --paper:#ededed;
  --dark:#221f1f;
  --footer:#262626;
  --footer-text:#c4c4c4;
  --white:#ffffff;
}
*{box-sizing:border-box;margin:0;padding:0}
html,body{width:1200px;height:2640px;overflow:hidden;background:var(--white)}
body{font-family:"Noto Serif",Georgia,serif;color:var(--ink);font-size:13px;line-height:1.45}
.page{position:relative;width:1200px;height:2640px;overflow:hidden}
.abs{position:absolute}
h2.section-title{font-family:"Lora",Georgia,serif;font-weight:400;font-size:26px;color:var(--blue)}

/* header */
.site-header{left:0;top:0;width:1200px;height:95px;background:#f7f7f7}
.brand{left:180px;top:24px;display:flex;align-items:center;gap:10px}
.brand-mark{width:34px;height:34px;background:var(--blue)}
.brand-name{font-family:"Lora",Georgia,serif;font-size:26px;color:var(--navy);font-weight:400;letter-spacing:1px}
.call{left:855px;top:20px;color:var(--blue);font-size:15px;display:flex;align-items:center;gap:8px}
.nav{left:548px;top:50px;display:flex;gap:22px;font-size:13px;color:#222}
.nav .active{color:var(--blue)}
.nav .services{color:var(--blue)}
.socials{left:952px;top:50px;display:flex;gap:14px}
.socials span{width:11px;height:11px;border-radius:50%;background:#333;display:block;margin-top:3px}
.dropdown{left:600px;top:88px;width:140px;background:#fff;padding:6px 10px;font-size:11px;line-height:23px;color:#333;box-shadow:0 2px 6px rgba(0,0,0,.15);z-index:5}

/* hero */
.hero{left:0;top:95px;width:1200px;height:375px;background:linear-gradient(180deg,#b9c9c8 0%,#6f7d70 45%,#4f6a3c 100%)}
.hero-title{left:200px;top:243px;font-family:"Lora",serif;font-size:28px;color:var(--cyan)}
.hero-text{left:200px;top:290px;width:380px;font-size:15px;font-weight:700;color:#fff;line-height:1.3}
.btn-blue{background:var(--blue);color:#fff;font-size:15px;padding:8px 20px;border:2px solid #fff;display:inline-block}
.hero-btn{left:200px;top:347px}

/* band */
.quote-band{left:0;top:470px;width:1200px;height:58px;background:var(--cyan)}
.quote-band p{position:absolute;left:173px;top:18px;color:#fff;font-weight:700;font-size:15px}
.quote-btn{position:absolute;left:912px;top:12px;background:#fff;color:var(--blue);padding:5px 14px;font-size:15px}

/* intro */
.intro{left:0;top:528px;width:1200px;height:472px;background:var(--paper)}
.col-title{top:548px}
.about-photo{left:173px;top:588px;width:268px;height:195px;background:linear-gradient(180deg,#9cb6cc,#c9c5bd 60%,#6f7b5e)}
.about-text{left:183px;top:798px;width:250px;color:var(--muted);font-size:12px}
.about-text p{margin-bottom:12px}
.read-more{background:var(--blue);color:#fff;font-size:11px;padding:3px 8px;border:1px solid #fff;display:inline-block}
.read-more.outline{background:#fff;color:#333;border:1px solid #333}
.why-list{left:465px;top:598px;width:275px}
.why-item{display:flex;gap:14px;margin-bottom:22px;color:var(--muted);font-size:12px;line-height:1.35}
.why-item svg{flex:none;margin-top:4px}
.splash{left:760px;top:585px;width:262px;height:380px;background:var(--blue);border-radius:6px 22px 10px 30px}
.contact-form{left:776px;top:598px;width:230px;color:#fff;font-size:12px;font-weight:700}
.contact-form label{display:block}
.contact-form .field{height:22px;border:1px solid #9fd2f5;margin:5px 0 13px 4px;width:222px}
.submit-btn{display:inline-block;background:var(--cyan);color:#fff;font-weight:400;font-size:13px;padding:3px 22px;margin-top:6px;border:1px solid #fff}

/* work */
.work{left:0;top:1000px;width:1200px;height:545px;background:var(--dark)}
.work-title{left:0;width:1200px;top:1018px;text-align:center;color:#fff;font-family:"Lora",serif;font-weight:400;font-size:24px}
.rule{height:2px;width:62px;background:var(--cyan)}
.work-grid{left:0;top:1085px;width:1200px;display:grid;grid-template-columns:repeat(4,300px);grid-auto-rows:189px}
.tile{position:relative}
.tile-caption{position:absolute;left:28px;top:118px;color:#fff;font-weight:700;font-size:13px}
.tile-caption .read-more{margin-top:10px;display:block;width:max-content}

/* services */
.services-sec{left:0;top:1545px;width:1200px;height:365px;background:var(--paper)}
.arrows{left:970px;top:1590px;display:flex;gap:5px}
.arrows span{width:24px;height:24px;border:1px solid #333;display:flex;align-items:center;justify-content:center;background:#fff}
.arrows span.on{background:var(--blue);border-color:var(--blue)}
.card{top:1632px;width:265px}
.card-img{height:130px}
.card h3{font-weight:400;color:var(--blue);font-size:15px;margin:13px 0 8px 10px}
.card p{color:var(--muted);font-size:12px;margin:0 10px 8px;line-height:1.35}
.card .read-more{margin-left:10px}

/* cta */
.cta{left:0;top:1910px;width:1200px;height:375px;background:linear-gradient(135deg,#1e5a92,#16457a 60%,#0f3560)}
.paint-can{left:820px;top:2050px;width:180px;height:215px;background:linear-gradient(180deg,#a8323c,#d9c9bd)}
.cta-title{left:183px;top:2010px;font-family:"Lora",serif;font-weight:700;font-size:39px;color:#fff}
.cta-sub{left:183px;top:2068px;font-family:"Lora",serif;font-size:30px;color:#fff}
.cta-btn{left:183px;top:2164px;background:#fff;color:var(--blue);font-size:23px;padding:6px 22px}

/* footer */
.footer{left:0;top:2285px;width:1200px;height:315px;background:var(--footer)}
.follow{left:178px;top:2308px;background:var(--cyan);color:#222;font-size:12px;padding:8px 22px;display:flex;align-items:center;gap:8px}
.follow i{width:18px;height:18px;border:1.5px solid #fff;border-radius:50%;display:block}
.fcol{top:2370px;font-size:12px;color:var(--footer-text)}
.fcol h4{color:#fff;font-size:13px;font-weight:700;margin-bottom:18px;letter-spacing:.5px}
.fcol .bold{color:#e0e0e0;font-weight:700;margin-bottom:14px}
.links{display:grid;grid-template-columns:90px 100px;row-gap:14px}
.links .hl{color:var(--cyan)}
.news-input{width:185px;height:20px;background:#555;color:#aaa;font-size:10px;padding:3px 6px;margin:12px 0 8px}
.news-btn{background:var(--cyan);color:#fff;font-size:10px;padding:2px 6px;display:inline-block}
.contact-list div{display:flex;gap:14px;margin-bottom:10px}
.contact-list svg{flex:none;margin-top:3px}
.bottom-bar{left:0;top:2600px;width:1200px;height:40px;background:var(--blue);color:#fff;font-size:11px}
.bottom-bar p{position:absolute;left:183px;top:12px}
.to-top{position:absolute;left:1045px;top:5px;width:30px;height:30px;border:1px solid #6fa8d8;display:flex;align-items:center;justify-content:center}
</style>
</head>
<body>
<div class="page">

  <header class="site-header abs"></header>
  <div class="brand abs"><span class="brand-mark"></span><span class="brand-name">Bluefinch Painting</span></div>
  <div class="call abs">
    <svg width="14" height="14" viewBox="0 0 24 24"><path fill="#1b72bd" d="M6.6 10.8a15.2 15.2 0 0 0 6.6 6.6l2.2-2.2c.3-.3.7-.4 1-.2 1.1.4 2.3.6 3.6.6.6 0 1 .4 1 1V20c0 .6-.4 1-1 1A17 17 0 0 1 3 4c0-.6.4-1 1-1h3.5c.6 0 1 .4 1 1 0 1.3.2 2.5.6 3.6.1.3 0 .7-.2 1z"/></svg>
    Call : (555) 318-7046
  </div>
  <nav class="nav abs">
    <span class="active">Home</span><span class="services">Services ▾</span><span>Who We Are</span><span>Projects</span><span>Contact Us</span>
  </nav>
  <div class="socials abs"><span></span><span></span><span></span></div>

  <div class="hero abs" role="img" aria-label="Photo of a large two-storey family house with a stone front and green garden"></div>
  <div class="dropdown abs">
    <div>Necessitatibus Saepe</div><div>Soluta Nobis</div><div>Temporibus Autem</div><div>Reiciendis Volupta</div><div>Debitis Autenim</div>
  </div>
  <div class="hero-title abs">Your Dream Home</div>
  <div class="hero-text abs">Accusamus et iusto odio dignissimos ducimus qui blanditiis praesentium voluptatum</div>
  <div class="hero-btn abs btn-blue">View More ›</div>

  <section class="quote-band abs">
    <p>Sed ut perspiciatis unde omnis iste natus error sit voluptatem</p>
    <span class="quote-btn">Get A Quote</span>
  </section>

  <section class="intro abs"></section>
  <h2 class="section-title abs col-title" style="left:173px">About us</h2>
  <h2 class="section-title abs col-title" style="left:465px">Why Choose Us</h2>
  <h2 class="section-title abs col-title" style="left:757px">Quick Contact</h2>

  <div class="about-photo abs" role="img" aria-label="Photo of the company pickup truck and work van parked outside a house"></div>
  <div class="about-text abs">
    <p>Eos qui ratione voluptatem sequi nesciunt. Neque porro quisquam est, qui dolorem ipsum quia dolor.</p>
    <p>Ullam corporis suscipit laboriosam, nisi ut aliquid ex ea commodi consequatur.</p>
    <span class="read-more">Read More</span>
  </div>

  <div class="why-list abs">
    <div class="why-item">
      <svg width="26" height="26" viewBox="0 0 26 26"><rect x="2" y="3" width="16" height="7" rx="1" fill="#3ec3f0"/><path d="M18 6h3v7H12v4" stroke="#3ec3f0" stroke-width="2" fill="none"/><rect x="10" y="17" width="4" height="8" fill="#3ec3f0"/></svg>
      <p>Perspiciatis unde omnis iste natus error sit voluptatem accusantium doloremque laudantium, totam rem aperiam</p>
    </div>
    <div class="why-item">
      <svg width="26" height="26" viewBox="0 0 26 26"><rect x="2" y="3" width="16" height="7" rx="1" fill="#3ec3f0"/><path d="M18 6h3v7H12v4" stroke="#3ec3f0" stroke-width="2" fill="none"/><rect x="10" y="17" width="4" height="8" fill="#3ec3f0"/></svg>
      <p>Nam libero tempore, cum soluta nobis est eligendi optio cumque nihil imp edit quo minus id quod maxime est placeat facere possimus</p>
    </div>
    <div class="why-item">
      <svg width="26" height="26" viewBox="0 0 26 26"><rect x="2" y="3" width="16" height="7" rx="1" fill="#3ec3f0"/><path d="M18 6h3v7H12v4" stroke="#3ec3f0" stroke-width="2" fill="none"/><rect x="10" y="17" width="4" height="8" fill="#3ec3f0"/></svg>
      <p>Soluta nobis est eligendi optio cum que nihil impedit quo minus id quod maxime placeat facere possimus, omnis voluptas assumenda</p>
    </div>
    <div class="why-item">
      <svg width="26" height="26" viewBox="0 0 26 26"><rect x="2" y="3" width="16" height="7" rx="1" fill="#3ec3f0"/><path d="M18 6h3v7H12v4" stroke="#3ec3f0" stroke-width="2" fill="none"/><rect x="10" y="17" width="4" height="8" fill="#3ec3f0"/></svg>
      <p>Omnis dolor repellendus. Temporibus autem quibusdam et aut officiis debitis aut rerum necessitatibus saepe eveniet ut et voluptates</p>
    </div>
  </div>

  <div class="splash abs" role="img" aria-label="Broad blue paint stroke with a paintbrush at its lower right corner"></div>
  <form class="contact-form abs">
    <label>Name :</label><div class="field"></div>
    <label>Phone Number :</label><div class="field"></div>
    <label>Address :</label><div class="field"></div>
    <label>E-mail :</label><div class="field"></div>
    <label>Painting project description :</label><div class="field"></div>
    <span class="submit-btn">Submit</span>
  </form>

  <section class="work abs"></section>
  <h2 class="work-title abs">Our Work</h2>
  <div class="rule abs" style="left:569px;top:1056px"></div>
  <div class="work-grid abs">
    <div class="tile" role="img" aria-label="Company work van with lettering on its side" style="background:linear-gradient(180deg,#c8d0d6,#f2f2f2 45%,#8e9a8a)"></div>
    <div class="tile" role="img" aria-label="Hand rolling paint onto a patterned wall" style="background:linear-gradient(135deg,#b7b3ad,#dcd8d2)"></div>
    <div class="tile" role="img" aria-label="Freshly painted house front with gable" style="background:linear-gradient(180deg,#7c8892,#b4ab9c 60%,#6d8a52)"></div>
    <div class="tile" role="img" aria-label="Paint supplier sign stating that quality paint is used" style="background:linear-gradient(180deg,#eeeeee,#d9d9d9)"></div>
    <div class="tile" role="img" aria-label="Painter brushing a white window frame while holding a paint can" style="background:linear-gradient(135deg,#c9c4bd,#efece8)"></div>
    <div class="tile" role="img" aria-label="Painted house exterior under a dark overlay" style="background:linear-gradient(180deg,#3a3a3a,#2a2a2a)">
      <div class="tile-caption">REPUDIANDAE SINT<span class="read-more">Read More</span></div>
    </div>
    <div class="tile" role="img" aria-label="Painter in hard hat rolling paint on an exterior wall" style="background:linear-gradient(135deg,#e9e6e0,#8d9aa8)"></div>
    <div class="tile" role="img" aria-label="Company truck and vans parked in front of a house" style="background:linear-gradient(180deg,#b3c7d8,#d8d3c8 55%,#8b9870)"></div>
  </div>

  <section class="services-sec abs"></section>
  <h2 class="section-title abs" style="left:173px;top:1575px;color:#333">What We Do</h2>
  <div class="rule abs" style="left:173px;top:1615px"></div>
  <div class="arrows abs">
    <span class="on"><svg width="8" height="10"><path d="M6 1 2 5l4 4" stroke="#fff" stroke-width="1.5" fill="none"/></svg></span>
    <span><svg width="8" height="10"><path d="m2 1 4 4-4 4" stroke="#333" stroke-width="1.5" fill="none"/></svg></span>
  </div>
  <article class="card abs" style="left:173px">
    <div class="card-img" role="img" aria-label="Hands pressing a rag onto a red painted wall" style="background:linear-gradient(135deg,#d9726d,#c85b58)"></div>
    <h3>Ragging Wall Paint</h3>
    <p>Ut aut reiciendis voluptatibus maiores alias consequatur aut perferendis doloribus asperiores repellat</p>
    <span class="read-more">Read More</span>
  </article>
  <article class="card abs" style="left:465px">
    <div class="card-img" role="img" aria-label="Gloved hand dabbing a sponge on a textured wall" style="background:linear-gradient(135deg,#3f4a4d,#5d6669)"></div>
    <h3>Sponging Wall Paint</h3>
    <p>Ut aut reiciendis voluptatibus maiores alias consequatur aut perferendis doloribus asperiores repellat</p>
    <span class="read-more outline">Read More</span>
  </article>
  <article class="card abs" style="left:757px">
    <div class="card-img" role="img" aria-label="Artist on a ladder painting a mural on a warm-toned wall" style="background:linear-gradient(135deg,#c98a4e,#e9c68f)"></div>
    <h3>Mural Wall Paint</h3>
    <p>Ut aut reiciendis voluptatibus maiores alias consequatur aut perferendis doloribus asperiores repellat</p>
    <span class="read-more outline">Read More</span>
  </article>

  <section class="cta abs" role="img" aria-label="Blue-tinted photo of a house as background"></section>
  <svg class="abs" style="left:0;top:1910px" width="1200" height="375" viewBox="0 0 1200 375">
    <path d="M1120 0H1200V375H700C900 340 1080 220 1120 0Z" fill="#e4e6e8"/>
    <path d="M1120 0C1080 220 900 340 700 375" stroke="#3ec3f0" stroke-width="8" fill="none"/>
  </svg>
  <div class="paint-can abs" role="img" aria-label="Photo of an open paint can with red paint dripping down its side and a brush laid across the top"></div>
  <div class="cta-title abs">Colour Your Dream Home</div>
  <div class="cta-sub abs">In An Affordable Price</div>
  <div class="cta-btn abs">Read More</div>

  <footer class="footer abs"></footer>
  <div class="follow abs">Follow us on <i></i><i></i><i></i></div>
  <div class="fcol abs" style="left:183px;width:190px">
    <h4>ABOUT COMPANY</h4>
    <p class="bold">Rerum necessitatibus saepe eveniet ut et voluptates repudiandae sint</p>
    <p>Temporibus autem quibusdam et aut officiis debitis aut rerum necessitatibus.</p>
  </div>
  <div class="fcol abs" style="left:398px">
    <h4>QUICK LINKS</h4>
    <div class="links"><span>Home</span><span>Who We Are</span><span>Services</span><span>Latest News</span><span>Projects</span><span>Privacy Policy</span><span>Gallery</span><span class="hl">Contact Us</span></div>
  </div>
  <div class="fcol abs" style="left:617px;width:195px">
    <h4>NEWSLETTER</h4>
    <p>By subscribing to our mailing list you will get the latest news from us</p>
    <div class="news-input">Your email address</div>
    <span class="news-btn">Submit</span>
  </div>
  <div class="fcol abs contact-list" style="left:838px;width:230px">
    <h4>CONTACT US</h4>
    <div><svg width="12" height="12" viewBox="0 0 12 12"><path d="M11 1 1 5l4 1 1 5z" fill="#c4c4c4"/></svg><span>Oluptas assumenda est, Omnis dolor</span></div>
    <div><svg width="12" height="12" viewBox="0 0 24 24"><path fill="#c4c4c4" d="M6.6 10.8a15.2 15.2 0 0 0 6.6 6.6l2.2-2.2c.3-.3.7-.4 1-.2 1.1.4 2.3.6 3.6.6.6 0 1 .4 1 1V20c0 .6-.4 1-1 1A17 17 0 0 1 3 4c0-.6.4-1 1-1h3.5c.6 0 1 .4 1 1 0 1.3.2 2.5.6 3.6.1.3 0 .7-.2 1z"/></svg><span>(555) 318-7046</span></div>
    <div><svg width="12" height="10" viewBox="0 0 12 10"><rect x=".5" y=".5" width="11" height="9" fill="none" stroke="#c4c4c4"/><path d="m.5.5 5.5 5 5.5-5" stroke="#c4c4c4" fill="none"/></svg><span>info@bluefinchpainting.example</span></div>
    <div><svg width="12" height="12" viewBox="0 0 12 12"><rect x="1" y="4" width="10" height="6" fill="#c4c4c4"/><rect x="3" y="1" width="6" height="3" fill="none" stroke="#c4c4c4"/></svg><span>+12 3456 7890</span></div>
  </div>

  <div class="bottom-bar abs">
    <p>Copyright © Bluefinch</p>
    <span class="to-top"><svg width="10" height="10"><path d="m1 5 4-4 4 4M1 9l4-4 4 4" stroke="#fff" fill="none"/></svg></span>
  </div>

</div>
</body>
</html>
```